Aviation Maintenance Business Card Design Challenge

We are seeking a compelling and professional business card design for the owner of a newly established company, Harrow Aerotech, LLC, based out of QMTB – Dunmore County Airport (Tolland Field) in Lawrenceville, Georgia. The company specializes in aircraft maintenance and detailing services, providing top-tier care and precision to both private and corporate aircraft owners. This business card will represent the owner, founder and operator, a licensed A&P (Airframe and Powerplant) Mechanic with over 20 years of hands-on aviation maintenance experience. His reputation is built on technical expertise, reliability, and a commitment to excellence — qualities that Harrow Aerotech aims to reflect in every aspect of its brand, including its visual identity.

Designers are encouraged to include elements such as the QMTB airport code, contact info layout suitable for mobile and field-based communication, and company branding that balances technical skill with personalized service.

Target Market(s)

Aircraft owners and operators

Industry/Entity Type

Aviation

Contact Information for Business Card

Name: Ed Marcus Whitby, (555) 314-2290, harrowaerotechllc@mailbox.example, www.harrowaerotech.example, QMTB – Dunmore County Airport (Tolland Field) Lawrenceville, Georgia 30000

Requirements
Must have
• Aeronautical themes or visual cues, highlight the company’s dual services: maintenance and cleaning/detailing, emphasize the owner's credentials, experience, and role as the face of the business
Nice to have
• Company logo

```html
<!DOCTYPE html>
<html lang="en">
<head>
<meta charset="utf-8">
<title>Harrow Aerotech – Business Card</title>
<link href="https://fonts.googleapis.com/css2?family=Montserrat:wght@300&family=Roboto+Condensed:wght@400;700&display=swap" rel="stylesheet">
<style>
  :root {
    --page: #eeeff0;
    --navy: #0b1240;
    --teal: #0e8575;
    --ink: #0b1a4a;
    --sky: #5cc8ea;
    --sky-soft: #6fc6ec;
    --violet: #2e3797;
    --lime: #d4e86a;
    --leaf: #9bd66a;
  }
  * { margin: 0; padding: 0; box-sizing: border-box; }
  html, body { width: 1200px; height: 800px; overflow: hidden; background: var(--page); }
  body { position: relative; font-family: "Roboto Condensed", sans-serif; }

  .card { position: absolute; top: 73px; height: 653px; }
  .card--front { left: 104px; width: 451px; background: var(--navy); }
  .card--back { left: 642px; width: 427px; background: var(--teal); color: var(--ink); }

  .airport-code {
    position: absolute; left: 341px; top: 40px;
    font-weight: 700; font-size: 30px; letter-spacing: 1px; color: var(--sky);
  }
  .vertical { position: absolute; white-space: nowrap; transform-origin: left top; transform: rotate(-90deg); }
  .tagline {
    left: 330px; top: 510px;
    font-family: "Montserrat", sans-serif; font-weight: 300; font-size: 25px; color: var(--sky-soft);
  }
  .tagline-echo {
    left: 268px; top: 468px;
    font-family: "Montserrat", sans-serif; font-weight: 300; font-size: 16px; color: var(--violet);
  }
  .tagline-rule { position: absolute; left: 323px; top: 134px; width: 60px; height: 1px; background: #1c2560; }
  .company-name {
    left: 168px; top: 440px;
    font-weight: 700; font-size: 46px; line-height: 46px; text-transform: uppercase; color: var(--leaf);
  }

  .owner-name { position: absolute; left: 40px; top: 50px; font-weight: 700; font-size: 39px; text-transform: uppercase; }
  .owner-role { position: absolute; left: 40px; top: 104px; font-size: 27px; text-transform: uppercase; }
  .services {
    position: absolute; left: 40px; top: 166px;
    font-weight: 700; font-size: 29px; line-height: 34px; letter-spacing: .5px; color: var(--lime); text-transform: uppercase;
  }
  .contacts { position: absolute; left: 38px; top: 275px; list-style: none; }
  .contact { display: flex; align-items: center; height: 48.5px; font-size: 25px; }
  .contact--email { font-size: 22.5px; }
  .contact-icon { width: 31px; height: 31px; margin-right: 13px; flex: none; }
  .tool-badge { position: absolute; left: 224px; top: 437px; width: 175px; height: 198px; }
</style>
</head>
<body>
  <section class="card card--front">
    <div class="airport-code">QMTB</div>
    <div class="tagline-rule"></div>
    <div class="vertical company-name">Harrow<br>Aerotech</div>
    <div class="vertical tagline-echo">The Sky Is Never The Limit</div>
    <div class="vertical tagline">The Sky Is Never The Limit</div>
  </section>

  <section class="card card--back">
    <h1 class="owner-name">Ed Marcus Whitby</h1>
    <p class="owner-role">Owner / A&amp;P Mechanic</p>
    <p class="services">Aircraft Maintenance<br>&amp; Detailing</p>
    <ul class="contacts">
      <li class="contact">
        <svg class="contact-icon" viewBox="0 0 32 32"><circle cx="16" cy="16" r="16" fill="var(--ink)"/><path d="M11 9.5l3 3-1.6 2a10 10 0 0 0 5.1 5.1l2-1.6 3 3-2 2.2C15 23 9 17 8.8 11.5z" fill="var(--teal)"/></svg>
        (555) 314-2290
      </li>
      <li class="contact contact--email">
        <svg class="contact-icon" viewBox="0 0 32 32"><circle cx="16" cy="16" r="16" fill="var(--ink)"/><rect x="9" y="11" width="14" height="10" rx="1" fill="var(--teal)"/><path d="M9.5 11.5L16 17l6.5-5.5" fill="none" stroke="var(--ink)" stroke-width="1.5"/></svg>
        harrowaerotechllc@mailbox.example
      </li>
      <li class="contact">
        <svg class="contact-icon" viewBox="0 0 32 32"><circle cx="16" cy="16" r="16" fill="var(--ink)"/><g fill="none" stroke="var(--teal)" stroke-width="1.6"><circle cx="16" cy="16" r="7"/><ellipse cx="16" cy="16" rx="3" ry="7"/><path d="M9 16h14M10 12.5h12M10 19.5h12"/></g></svg>
        www.harrowaerotech.example
      </li>
    </ul>
    <svg class="tool-badge" viewBox="0 0 175 198" role="img" aria-label="Maintenance and detailing tools icon in a hexagon badge">
      <path d="M87.5 4 L168 50 V148 L87.5 194 L7 148 V50 Z" fill="#0c6b60"/>
    </svg>
  </section>
</body>
</html>
```